Brimvane.com fiber optic internet website redesign

We need a new website design for our fiber optic internet company that provides internet, phone, and tv services. It should use the text "Marrowfen fiber optics", and "I beamed up with Marrowfen". The design should use the color blue and the attached logo.
We are a 30 year old internet company who started as a dial up internet provider in our basement. Today we design, build, and maintain our own fiber optic internet network to provide service to residential, business, educational, healthcare, and governmental customers

```html
<!DOCTYPE html>
<html lang="en">
<head>
<meta charset="utf-8">
<title>Marrowfen fiber optics</title>
<link href="https://fonts.googleapis.com/css2?family=Poppins:wght@300;400;500;600;700&display=swap" rel="stylesheet">
<style>
:root{
  --blue:#0b4aa2;
  --blue-deep:#062a6b;
  --navy:#031a45;
  --ink:#2b2b2b;
  --grey:#f3f3f5;
  --pale:#eaf1fb;
  --line:#b9b9b9;
  --white:#ffffff;
}
*{margin:0;padding:0;box-sizing:border-box}
html,body{width:1200px;height:5213px;overflow:hidden}
body{font-family:'Poppins',sans-serif;color:var(--ink);background:var(--white);position:relative}
.abs{position:absolute}
section{position:absolute;left:0;width:1200px}
.h2{position:absolute;font-weight:400;color:var(--blue);font-size:52px;line-height:1;white-space:nowrap}
.center{left:0;width:1200px;text-align:center}
.rule{position:absolute;height:2px;background:#bfbfbf}
.btn{position:absolute;background:var(--blue);color:#fff;border-radius:30px;font-size:27px;display:flex;align-items:center;justify-content:center}
.fill{position:absolute}

/* header */
.header{top:0;height:142px}
.brand{position:absolute;display:flex;align-items:center;gap:14px;font-weight:600;color:var(--blue)}
.brand .dot{border-radius:50%;background:var(--blue)}
.topline{position:absolute;top:36px;right:66px;display:flex;gap:34px;color:#fff;font-size:14px;align-items:center}
.topline span{display:flex;align-items:center;gap:10px}
.nav{position:absolute;top:88px;right:66px;display:flex;color:#fff;font-size:14px}
.nav a{color:#fff;text-decoration:none;padding:0 9px;border-right:1.5px solid #fff;line-height:1}
.nav a:last-child{border-right:none;padding-right:0}

/* hero */
.hero{top:142px;height:600px}
.hero h1{position:absolute;left:69px;top:84px;font-size:88px;font-weight:400;color:#fff;line-height:92px}
.hero p{position:absolute;left:70px;top:298px;width:470px;font-size:13px;color:#fff;line-height:17px}
.hero .ghost{position:absolute;left:69px;top:378px;width:218px;height:54px;border:2px solid #fff;border-radius:30px;color:#fff;font-size:22px;display:flex;align-items:center;justify-content:center}

/* why */
.why{top:729px;height:542px;background:var(--grey)}
.feature{position:absolute;width:260px;text-align:center;font-size:27px;color:#444;line-height:32px}
.badge{position:absolute;width:174px;height:174px;border-radius:50%;border:4px solid var(--blue);display:flex;align-items:center;justify-content:center}
.badge::after{content:"";position:absolute;inset:8px;border-radius:50%;border:3px dotted var(--blue)}

/* service bands */
.res{top:1271px;height:565px;background:var(--pale)}
.biz{top:1836px;height:568px;background:#f1f1f3}
.list{position:absolute;list-style:none;font-size:31px;font-weight:500;color:#222}
.list li{height:48px;display:flex;align-items:center;gap:22px}
.list li::before{content:"";width:14px;height:14px;border-radius:50%;background:#9a9a9a}
.ring{position:absolute;border-radius:50%;background:#cfcfd2;box-shadow:0 0 0 6px #e3e3e6}
.ring .fill{border-radius:50%}

/* services grid */
.services{top:2404px;height:523px;background:#eef3fb}
.card{position:absolute;top:215px;width:241px;height:241px;background:var(--blue);color:#fff;font-size:27px;font-weight:500;line-height:32px;text-align:center}
.card .fill{left:0;top:0;width:241px;height:136px}
.card .label{position:absolute;left:0;right:0;top:136px;bottom:0;display:flex;align-items:center;justify-content:center}

/* pricing */
.pricing{top:2927px;height:356px;background:var(--blue)}
.price{position:absolute;top:0;height:356px;text-align:center;color:#fff}
.price b{display:block;margin-top:112px;font-size:64px;font-weight:600;line-height:70px}
.price span{display:block;margin-top:14px;font-size:20px;line-height:24px}
.vr{position:absolute;top:24px;width:1.5px;height:318px;background:#6d93cf}

/* faq */
.faq{top:3283px;height:603px;background:linear-gradient(180deg,#eef3fb,#e4edf9)}
.acc{position:absolute;left:77px;width:522px;border:2px solid var(--blue);border-radius:8px;background:#fff}
.acc h4{position:absolute;left:12px;top:18px;font-size:15px;font-weight:500;color:var(--blue)}
.acc .pm{position:absolute;right:26px;width:20px;height:20px;border-radius:50%;background:var(--blue);color:#fff;font-size:16px;line-height:20px;text-align:center}
.acc p{position:absolute;left:12px;top:43px;width:490px;font-size:12.5px;line-height:15px;color:#444;text-align:justify}

/* contact */
.contact{top:3886px;height:810px;background:#fff}
.contact .intro{position:absolute;left:0;width:1200px;top:192px;text-align:center;font-size:13.5px;line-height:22px;color:#333}
.panel{position:absolute;left:593px;top:300px;width:504px;height:368px;background:var(--grey)}
.field{position:absolute;background:#fff;border:1px solid #e2e2e2;font-size:14px;color:#a9a9a9;padding:14px 10px}
.submit{position:absolute;left:28px;top:317px;width:72px;height:23px;border-radius:12px;background:var(--blue);color:#fff;font-size:13px;display:flex;align-items:center;justify-content:center}

/* footer */
.footer{top:4696px;height:517px;background:#f0f2f5}
.fh{position:absolute;top:106px;font-size:22px;font-weight:500;color:var(--blue)}
.links{position:absolute;left:336px;top:165px;list-style:none;font-size:13px;color:#333}
.links li{height:30px;display:flex;align-items:center;gap:18px}
.links li::before,.hours li::before{content:"";width:6px;height:6px;border-radius:50%;background:var(--blue)}
.hours{position:absolute;left:851px;top:163px;list-style:none;font-size:16px;color:#222}
.hours li{height:30px;display:flex;align-items:center;gap:14px}
.crow{position:absolute;left:557px;display:flex;gap:10px;font-size:16px;line-height:23px;color:#222}
.crow .ic{flex:none;width:38px;height:38px;border-radius:50%;background:var(--blue);display:flex;align-items:center;justify-content:center;margin-top:10px}
.social{position:absolute;top:4969px;width:36px;height:36px;border-radius:50%;background:var(--blue)}
.copy{position:absolute;left:0;width:1200px;top:5166px;text-align:center;font-size:13px;color:#333}
</style>
</head>
<body>

<!-- header -->
<header class="header abs" style="left:0;width:1200px">
  <svg class="abs" style="left:0;top:0" width="1200" height="142" viewBox="0 0 1200 142">
    <path d="M0 0H436C420 40 422 100 445 142H0Z" fill="#fff"/>
    <path d="M436 0H1200V142H445C422 100 420 40 436 0Z" fill="var(--blue)"/>
  </svg>
  <div class="brand" style="left:70px;top:38px;font-size:38px">
    <span class="dot" style="width:66px;height:66px"></span>Marrowfen
  </div>
  <div class="topline">
    <span><svg width="22" height="22" viewBox="0 0 22 22"><rect x="1" y="1" width="20" height="20" rx="5" fill="none" stroke="#fff" stroke-width="1.6"/><path d="M7 6c0 5 4 10 9 10l1-2-2.5-1.5-1.5 1c-2-1-3-2-4-4l1-1.5L8.5 5Z" fill="#fff"/></svg>555-014-2290</span>
    <span><svg width="22" height="22" viewBox="0 0 22 22"><rect x="1" y="1" width="20" height="20" rx="5" fill="none" stroke="#fff" stroke-width="1.6"/><rect x="6" y="7" width="10" height="8" fill="#fff"/><path d="M6 7l5 4 5-4" stroke="var(--blue)" fill="none"/></svg>sales@brimvane.com</span>
  </div>
  <nav class="nav">
    <a>Home</a><a>Residential</a><a>Business</a><a>Services</a><a>FAQ</a><a>Telecom</a><a>Contact us</a><a>Users</a><a>Support</a>
  </nav>
</header>

<!-- hero -->
<section class="hero">
  <svg class="abs" style="left:0;top:0" width="1200" height="600" viewBox="0 0 1200 600" role="img" aria-label="Glowing blue fiber optic light points on a dark background">
    <defs>
      <radialGradient id="heroGlow" cx="0.68" cy="0.4" r="0.6">
        <stop offset="0" stop-color="#1d5fe0"/>
        <stop offset="0.55" stop-color="#0a3a92"/>
        <stop offset="1" stop-color="#041c4f"/>
      </radialGradient>
    </defs>
    <path d="M0 0H1200V494C1000 580 760 600 600 587C380 570 160 520 0 485Z" fill="url(#heroGlow)"/>
  </svg>
  <h1>I Beamed Up With<br>Marrowfen</h1>
  <p>Fiber optic-based communications have been used for years by government and industry</p>
  <div class="ghost">Know More</div>
</section>

<!-- why choose -->
<section class="why" style="z-index:-1;top:680px;height:591px"></section>
<div class="h2 center" style="top:813px">Why Choose US</div>
<div class="rule" style="left:506px;top:900px;width:188px"></div>

<div class="badge" style="left:198px;top:951px">
  <svg width="90" height="90" viewBox="0 0 90 90" fill="none" stroke="var(--blue)" stroke-width="4" stroke-linecap="round" stroke-linejoin="round"><circle cx="45" cy="30" r="22"/><path d="M52 22c-3-4-16-4-16 3s16 3 16 10-13 7-16 3M44 14v32M32 58v22l-6-6M45 58v24l-6-6M45 82l6-6M58 58v22l6-6M32 80l6-6"/></svg>
</div>
<div class="badge" style="left:512px;top:951px">
  <svg width="96" height="96" viewBox="0 0 96 96" fill="none" stroke="var(--blue)" stroke-width="4" stroke-linejoin="round"><path d="M48 6l9 7 11-2 4 10 10 5-2 11 7 9-7 9 2 11-10 5-4 10-11-2-9 7-9-7-11 2-4-10-10-5 2-11-7-9 7-9-2-11 10-5 4-10 11 2Z"/><circle cx="48" cy="48" r="24"/><path d="M37 48l8 8 15-15" stroke-linecap="round"/></svg>
</div>
<div class="badge" style="left:820px;top:951px">
  <svg width="96" height="96" viewBox="0 0 96 96" fill="none" stroke="var(--blue)" stroke-width="4" stroke-linejoin="round"><path d="M42 8h12l2 10 8 4 9-6 8 8-6 9 4 8 10 2v12l-10 2-4 8 6 9-8 8-9-6-8 4-2 10H42l-2-10-8-4-9 6-8-8 6-9-4-8-10-2V42l10-2 4-8-6-9 8-8 9 6 8-4Z"/><path d="M40 36h14l4 6v16H40Z"/><circle cx="62" cy="62" r="10"/><path d="M57 62l4 4 6-7" stroke-linecap="round"/></svg>
</div>
<div class="feature" style="left:155px;top:1143px">low cost</div>
<div class="feature" style="left:469px;top:1143px">high quality</div>
<div class="feature" style="left:777px;top:1143px">extremely<br>reliable</div>

<!-- residential -->
<section class="res">
  <div class="h2" style="left:79px;top:100px;font-size:54px">Residential Services</div>
  <div class="rule" style="left:79px;top:176px;width:188px"></div>
  <ul class="list" style="left:85px;top:219px">
    <li>Internet Service</li><li>VoIP Phone Service</li><li>Video Service</li>
  </ul>
  <div class="btn" style="left:79px;top:401px;width:176px;height:48px">View More</div>
  <div class="ring" style="left:631px;top:34px;width:498px;height:498px">
    <div class="fill" role="img" aria-label="Photo of a network cable plug among glowing cyan fiber strands" style="left:30px;top:18px;width:444px;height:444px;background:radial-gradient(circle at 40% 35%,#7fe3f0,#1f8fb0 45%,#0b3c58 80%,#06202f)"></div>
  </div>
</section>

<!-- business -->
<section class="biz">
  <div class="ring" style="left:83px;top:36px;width:498px;height:498px">
    <div class="fill" role="img" aria-label="Photo of violet glowing fiber optic strands above network cable plugs" style="left:34px;top:22px;width:440px;height:440px;background:radial-gradient(circle at 50% 30%,#8b6bff,#4a2ad0 35%,#1a0f55 70%,#090520)"></div>
  </div>
  <div class="h2" style="left:636px;top:72px;font-size:54px">Business Services</div>
  <ul class="list" style="left:640px;top:176px">
    <li>SOHO Internet</li><li>Enterprise Internet</li><li>VoIP Phone Service</li><li>Hosted PBX Service</li><li>Metro-E/Layer 2 Service</li>
  </ul>
  <div class="btn" style="left:636px;top:445px;width:174px;height:49px">View More</div>
</section>

<!-- services -->
<section class="services">
  <div class="h2 center" style="top:74px">Services</div>
  <div class="rule" style="left:506px;top:144px;width:188px"></div>
  <div class="card" style="left:73px"><div class="fill" role="img" aria-label="Network of connected app icons on a dark background" style="background:linear-gradient(135deg,#2b3038,#4a5058)"></div><div class="label">Colocation</div></div>
  <div class="card" style="left:342px"><div class="fill" role="img" aria-label="Cloud hosting illustration over a city skyline" style="background:linear-gradient(180deg,#c9d3de,#7a8796)"></div><div class="label">Managed<br>Hosting</div></div>
  <div class="card" style="left:615px"><div class="fill" role="img" aria-label="Hand touching a glowing web hosting interface" style="background:linear-gradient(135deg,#0b2a66,#1f6fd6)"></div><div class="label">Virtual<br>Hosting</div></div>
  <div class="card" style="left:886px"><div class="fill" role="img" aria-label="Business meeting around a laptop" style="background:linear-gradient(135deg,#8a7868,#d9d3cc)"></div><div class="label">Service<br>Contracts</div></div>
</section>

<!-- pricing -->
<section class="pricing">
  <div class="price" style="left:63px;width:300px"><b>$55/mo</b><span>High Speed<br>Internet Service</span></div>
  <div class="vr" style="left:368px"></div>
  <div class="price" style="left:418px;width:300px"><b>$20/mo</b><span>VoIP Phone<br>Service</span></div>
  <div class="vr" style="left:739px"></div>
  <div class="price" style="left:770px;width:300px"><b>$80/mo</b><span>Phone &amp; Internet<br>Packages</span></div>
</section>

<!-- faq -->
<section class="faq">
  <div class="h2 center" style="top:75px">Frequently Asked Questions</div>
  <div class="rule" style="left:506px;top:146px;width:188px"></div>
  <div class="acc" style="top:206px;height:146px">
    <h4>What is burstable speed?</h4><div class="pm" style="top:16px">&minus;</div>
    <p>Burstable speed configurations are used by several of Marrowfen's competitors. Burstable speed give the appearance of faster speeds by only allowing very fast speeds within the first few seconds of every download. But for longer downloads, the burstable speed configuration lowers the download speeds to</p>
  </div>
  <div class="acc" style="top:376px;height:63px"><h4>How many email addresses do I get?</h4><div class="pm" style="top:20px">+</div></div>
  <div class="acc" style="top:457px;height:65px"><h4>What happens if my power goes out?</h4><div class="pm" style="top:21px">+</div></div>
  <div class="abs" style="left:729px;top:170px;width:388px;height:388px;border-radius:50%;border:3px solid var(--blue);padding:4px;background:#fff">
    <div role="img" aria-label="Photo of blue and magenta fiber optic strands" style="width:100%;height:100%;border-radius:50%;background:radial-gradient(circle at 65% 35%,#e06ad8,#6a3be0 30%,#1f72d8 55%,#0a2f6e 90%)"></div>
  </div>
</section>

<!-- contact -->
<section class="contact">
  <div class="h2 center" style="top:68px">Contact US</div>
  <div class="rule" style="left:506px;top:138px;width:188px"></div>
  <p class="intro">We would love to hear from you! Please use any of the methods of contact below and we will get back<br>to you as soon as possible. Thanks!</p>
  <svg class="abs" style="left:85px;top:258px" width="350" height="500" viewBox="0 0 350 500">
    <polygon points="5,40 300,5 345,460 45,490" fill="none" stroke="var(--blue)" stroke-width="2"/>
    <polygon points="38,20 320,30 310,478 28,470" fill="none" stroke="var(--blue)" stroke-width="2"/>
  </svg>
  <div class="fill" role="img" aria-label="Photo of cyan fiber optic strands on a dark background" style="left:123px;top:292px;width:270px;height:440px;background:linear-gradient(180deg,#9fe6f5,#1b8fc0 45%,#072b44 85%,#03121d)"></div>
  <div class="panel">
    <div class="field" style="left:28px;top:30px;width:215px;height:49px">First Name</div>
    <div class="field" style="left:269px;top:30px;width:215px;height:49px">Second Name</div>
    <div class="field" style="left:28px;top:109px;width:215px;height:49px">Phone</div>
    <div class="field" style="left:269px;top:109px;width:215px;height:49px">Email</div>
    <div class="field" style="left:28px;top:182px;width:460px;height:101px;padding-top:34px">Message</div>
    <div class="submit">Submit</div>
  </div>
</section>

<!-- footer -->
<footer class="footer abs" style="left:0;width:1200px;top:4696px;height:517px">
  <div class="brand" style="left:81px;top:180px;font-size:30px"><span class="dot" style="width:50px;height:50px"></span>Marrowfen</div>
  <div class="fh" style="left:336px">LINKS</div>
  <div class="fh" style="left:557px">CONTACT US</div>
  <div class="fh" style="left:848px">OFFICE HOURS</div>
  <ul class="links">
    <li>Product Benefits</li><li>How It Works</li><li>Customer Reviews</li><li>FAQ</li><li>Contact Us</li>
  </ul>
  <div class="crow" style="top:156px"><span class="ic"><svg width="18" height="22" viewBox="0 0 18 22"><path d="M9 1a7.5 7.5 0 0 0-7.5 7.5C1.5 14 9 21 9 21s7.5-7 7.5-12.5A7.5 7.5 0 0 0 9 1Z" fill="#fff"/><circle cx="9" cy="8.5" r="3" fill="var(--blue)"/></svg></span><div>ADDRESS:<br>Marrowfen Inc. 118, 9th<br>Street Larkhollow, PA 10482</div></div>
  <div class="crow" style="top:248px"><span class="ic"><svg width="20" height="20" viewBox="0 0 20 20"><path d="M4 2c0 8 6 15 14 15l1-3-4-2-2 2c-3-1-5-4-6-6l2-2-2-4Z" fill="#fff"/></svg></span><div>PHONE:<br>555-014-2290<br>Toll Free: 1-888-555-0147</div></div>
  <div class="crow" style="top:340px"><span class="ic"><svg width="20" height="16" viewBox="0 0 20 16"><rect x="1" y="1" width="18" height="14" fill="#fff"/><path d="M1 1l9 7 9-7" stroke="var(--blue)" stroke-width="1.6" fill="none"/></svg></span><div>EMAIL:<br>sales@brimvane.com<br>support@brimvane.com</div></div>
  <ul class="hours">
    <li>Sunday: 4pm - 8pm</li><li>Monday: 8am - 6pm</li><li>Tuesday: &nbsp;&nbsp;8am - 6pm</li><li>Wensday: &nbsp;8am - 6pm</li><li>Thursday: &nbsp;8am - 6pm</li><li>Friday: &nbsp;&nbsp;8am - 6pm</li><li>Saturday: &nbsp;12pm - 4pm</li>
  </ul>
  <div class="abs" style="left:67px;top:445px;width:1066px;height:1.5px;background:#9a9a9a"></div>
</footer>
<div class="social" style="left:116px"></div>
<div class="social" style="left:162px"></div>
<div class="social" style="left:211px"></div>
<div class="copy">© 2024 Company Name, Inc. All Rights Reserved.</div>

</body>
</html>
```